Webdesign für Birke Werkstatt
Zielgruppe
Birke Werkstatt produziert GfK Formteile und Abdeckungen
Einzelanfertigungen • Negativ - Formenbau • Prototyping • Ur-Modellbau
Formteile • Abdeckungen • Behälter • Sonderanfertigungen • Beschichtungen
Prototypen Modellbau • Anfertigung von Negativformen • Reparaturen • Fahrzeugteile
Hauptzielgruppe ist die Luftfahrtindustrie (Abdeckungen für Triebwerke)
Durch den Prototypenbau und die Einzelanfertigungen ist die Zielgruppe nicht klar zu definieren. Es werden Einzelteile jeglicher Art aus GfK hergestellt.
Dies können auch Anbauteile für PKW, Poolbeschichtungen, Teile für Boote etc sein.
Es gibt auch Kleinserien. Beispielsweise baut Birke-Werkstatt Motorhauben für Hallo-Brenner Rasenmähertrecker aus den 70er Jahren nach, die es nicht mehr zu kaufen gibt.
Aufgabenstellung
Der Designer hat alle Freiheiten. Die Seite muss natürlich responsiv funktionieren.
Außer dem Logo gibt es keine must-haves.
Schriftart aus dem Logo: EXO 2

```html
<!DOCTYPE html>
<html lang="de">
<head>
<meta charset="utf-8">
<title>Birke Werkstatt – Startseite</title>
<link href="https://fonts.googleapis.com/css2?family=Exo+2:wght@400;500;600;700;800&display=swap" rel="stylesheet">
<style>
:root{
  --blue:#1d5a8a;
  --blue-mid:#2467a0;
  --blue-light:#4a86bd;
  --text:#3b4450;
  --muted:#6f8aa3;
  --white:#fff;
  --footer:#eef2f6;
}
*{margin:0;padding:0;box-sizing:border-box}
html,body{width:788px;height:1200px;overflow:hidden;background:#fff}
body{font-family:"Exo 2",sans-serif;color:var(--text)}
.canvas{position:relative;width:788px;height:1200px;overflow:hidden}
.abs{position:absolute}

/* header */
.topbar{left:0;top:0;width:788px;height:68px;background:#fff}
.navbar{left:222px;top:26px;width:566px;height:42px;background:var(--blue);clip-path:polygon(18px 0,100% 0,100% 100%,0 100%)}
.header-line{left:0;top:60px;width:230px;height:2px;background:var(--blue)}
.brand{left:50px;top:16px;display:flex;align-items:center;gap:6px}
.brand-mark{width:30px;height:30px;background:var(--blue)}
.brand-name{font-size:17px;font-weight:700;color:var(--blue);line-height:1}
.brand-tag{left:86px;top:37px;font-size:5px;color:var(--blue)}
.phone-top{left:257px;top:5px;font-size:5.5px;color:var(--blue);line-height:1.3}
.phone-top b{font-weight:600}
.phone-top span{font-size:7px}
.lang{left:479px;top:9px;font-size:6px;color:var(--muted);display:flex;gap:4px;align-items:center}
.lang .flag{width:10px;height:6px;background:linear-gradient(#111 33%,#d00 33% 66%,#fc0 66%)}
.lang b{color:var(--blue);font-weight:600}
.legal-top{left:598px;top:9px;font-size:6px;color:var(--blue)}
.nav{left:257px;top:38px;display:flex;gap:0;font-size:7.6px;color:#fff}
.nav a{padding:5px 9.5px;color:#fff;text-decoration:none}
.nav a.active{background:#fff;color:var(--blue);font-weight:700}

/* hero */
.hero{left:0;top:68px;width:788px;height:236px;background:linear-gradient(110deg,#8f7458 0%,#b09476 35%,#7e7a5e 60%,#a58a6e 80%,#8d8a80 100%)}
.hero-title{left:50px;top:94px;color:#fff;font-size:13px;line-height:1.3}
.hero-title strong{font-size:21px;font-weight:800}
.hero-title .sub{font-size:7.5px;font-weight:600;opacity:.85}
.dots{left:13px;top:161px}
.dots i{display:block;width:4px;height:4px;border-radius:50%;background:#ddd;margin:0 0 3px 2px}
.dots i.on{width:7px;height:7px;margin-left:0;border:1.5px solid #fff;background:var(--blue)}
.btn{display:flex;align-items:center;justify-content:space-between;font-weight:700;font-size:8px;padding:0 13px}
.btn-white{background:#fff;color:var(--blue);clip-path:polygon(0 0,100% 0,98% 100%,0 100%)}
.btn-blue{background:var(--blue);color:#fff;clip-path:polygon(1.5% 0,100% 0,98.5% 100%,0 100%)}
.hero-btn{left:50px;top:158px;width:120px;height:27px}
.hero-btn .ic{display:flex;align-items:center;gap:6px}
.thumbs{left:49px;top:235px;display:flex;gap:6px}
.thumbs div{height:45px;border:2px solid #fff}
.arrows{left:733px;top:273px;display:flex;gap:2px}
.arrows div{width:16px;height:17px;background:#fff;display:flex;align-items:center;justify-content:center}
.arrows div.off{background:#ccd3da}
.dropdown{left:343px;top:68px;width:135px;background:var(--blue-mid);color:#fff;font-size:7px}
.dropdown .head{font-size:5.5px;font-weight:600;opacity:.7;padding:3px 10px 1px}
.dropdown .item{display:flex;justify-content:space-between;padding:6px 10px 7px;border-bottom:1px solid rgba(255,255,255,.25)}
.dropdown .item:last-child{border:0}

/* intro */
.intro{left:0;top:324px;width:788px;text-align:center}
.h-sec{font-size:16px;font-weight:700;color:var(--blue)}
.intro .tag{font-size:9px;color:var(--blue-mid)}
.intro p{font-size:7px;width:460px;margin:9px auto 0;line-height:1.3}
.feature{top:419px;width:160px;text-align:center}
.feature .num{position:absolute;top:2px;width:16px;height:16px;background:var(--blue);color:#fff;font-size:7px;font-weight:700;display:flex;align-items:center;justify-content:center}
.feature svg{display:block;margin:0 auto}
.feature h3{font-size:13px;font-weight:700;color:var(--blue);margin-top:12px}
.feature .kicker{font-size:7px;color:var(--blue-light);margin-top:2px}
.feature p{font-size:7px;line-height:1.3;margin-top:6px}
.about-btn{left:320px;top:567px;width:148px;height:28px}
.about-btn small{font-weight:400;font-size:6.5px;opacity:.8;display:flex;gap:8px;align-items:center}

/* trust band */
.band{left:0;top:622px;width:788px;height:185px;background:linear-gradient(90deg,#3f78ad 0%,#5a92c4 45%,#4b84b8 100%)}
.band-title{left:91px;top:657px;color:#fff;font-size:18px;line-height:1.1}
.band-title strong{font-size:22px;font-weight:800}
.band-text{left:91px;top:709px;width:340px;color:#fff;font-size:7.6px;line-height:1.3}
.band-btn{left:91px;top:742px;width:109px;height:27px}
.quote{left:480px;top:673px;width:171px;color:#fff;font-size:7px;line-height:1.3;text-align:justify}
.q-mark{color:#fff;font-size:16px;font-weight:700}
.q-name{left:480px;top:743px;width:171px;text-align:right;color:#fff;font-size:6.5px;line-height:1.3}
.q-name b{font-weight:700}

/* map */
.map-card{left:75px;top:792px;width:638px;height:180px;background:#fff}
.map{left:82px;top:800px;width:623px;height:164px;background:linear-gradient(135deg,#e9ebee 0%,#eeede6 55%,#e6e8ea 100%)}

/* contact */
.contact-h{left:98px;top:982px;font-size:15px}
.contact-sub{left:98px;top:1003px;font-size:9px;color:var(--blue)}
.contact-p{left:98px;top:1021px;width:241px;font-size:7px;line-height:1.3;text-align:justify}
.contact-btn{left:98px;top:1072px;width:109px;height:27px}
.cinfo{font-size:8px;font-weight:600;color:var(--blue);line-height:1.1}
.cinfo span{display:block;font-weight:400;font-size:12.5px;margin-top:2px}

/* footer */
.footer{left:0;top:1135px;width:788px;height:65px;background:var(--footer)}
.foot-mark{left:91px;top:1152px;width:26px;height:26px;background:var(--blue)}
.foot-text{left:135px;top:1154px;font-size:6px;line-height:1.5}
.foot-text .links{color:var(--blue)}
</style>
</head>
<body>
<div class="canvas">

  <!-- header -->
  <div class="abs topbar"></div>
  <div class="abs navbar"></div>
  <div class="abs header-line"></div>
  <div class="abs brand"><div class="brand-mark"></div><div class="brand-name">Birke Werkstatt</div></div>
  <div class="abs brand-tag">GfK Formteile | Ur-Modellbau | Prototyping</div>
  <div class="abs phone-top"><b>Telefon</b><br><span>+49 (0) 40 / 218 37 60</span></div>
  <div class="abs lang"><i class="flag"></i>deutsch | <b>Sprache wechseln ▾</b></div>
  <div class="abs legal-top">Impressum | Allgemeine Geschäftsbedingungen</div>
  <nav class="abs nav">
    <a class="active">Startseite</a><a>Über uns</a><a>Luftfahrt / Triebwerke</a><a>Formbauteile</a><a>Dekoration &amp; Kunstfelsen</a><a>Reparaturservice</a><a>Kontakt</a>
  </nav>

  <!-- hero -->
  <div class="abs hero" role="img" aria-label="Foto: Kunstfelsen mit Wasserfall in einer Poollandschaft"></div>
  <div class="abs hero-title">Naturechte <strong>Kunstfelsen</strong><br>für Schwimmbäder oder Freizeitparks<br><span class="sub">Schwimmbad / Sauna + Freizeitareas + Tierplastiken</span></div>
  <div class="abs dots"><i class="on"></i><i></i><i></i></div>
  <div class="abs btn btn-white hero-btn">
    <span class="ic"><svg width="12" height="11" viewBox="0 0 12 11"><ellipse cx="6" cy="9" rx="6" ry="2" fill="#1d5a8a"/><ellipse cx="6" cy="5.5" rx="4" ry="1.8" fill="#1d5a8a"/><ellipse cx="6" cy="2.2" rx="2.5" ry="1.5" fill="#1d5a8a"/></svg>Kunstfelsen</span>
    <svg width="6" height="8" viewBox="0 0 6 8"><path d="M1 1l3 3-3 3" stroke="#1d5a8a" stroke-width="1.3" fill="none"/></svg>
  </div>
  <div class="abs thumbs">
    <div style="width:66px;background:linear-gradient(#6d9a50,#35b5e6)" role="img" aria-label="Foto: Pool mit Felsen"></div>
    <div style="width:66px;background:linear-gradient(#88a070,#b8ad9a)" role="img" aria-label="Foto: Felsbau auf der Baustelle"></div>
    <div style="width:70px;background:linear-gradient(#b7a47d,#7d7a4a)" role="img" aria-label="Foto: Felswand mit Pflanzen"></div>
    <div style="width:65px;background:linear-gradient(#5c5650,#c8c3cf)" role="img" aria-label="Foto: Whirlpool in Felsgrotte"></div>
  </div>
  <div class="abs arrows">
    <div class="off"><svg width="5" height="7"><path d="M4 1L1.5 3.5 4 6" stroke="#8aa" fill="none"/></svg></div>
    <div><svg width="5" height="7"><path d="M1 1l2.5 2.5L1 6" stroke="#1d5a8a" stroke-width="1.2" fill="none"/></svg></div>
  </div>
  <div class="abs dropdown">
    <div class="head">Untermenü</div>
    <div class="item">Triebwerk-Abdeckungen<span>›</span></div>
    <div class="item">Aufblasbare Abdeckungen<span>›</span></div>
    <div class="item">Luftfahrt-Formbauteile<span>›</span></div>
  </div>

  <!-- intro -->
  <section class="abs intro">
    <h2 class="h-sec">Seit über 20 Jahren</h2>
    <div class="tag">Qualität. Kompetenz. Zuverlässig.</div>
    <p>Lorem ipsum dolor sit amet, consetetur sadipscing elitr, sed diam nonumy eirmod tempor invidunt ut labore et dolore magna aliquyam erat, sed diam voluptua. At vero eos et accusam et justo duo dolores et ea rebum.</p>
  </section>

  <div class="abs feature" style="left:81px">
    <div class="num" style="left:44px">1.</div>
    <svg width="40" height="44" viewBox="0 0 40 44" fill="none" stroke="#1d5a8a" stroke-width="1.6"><circle cx="20" cy="13" r="9"/><path d="M3 43v-6c0-6 7-10 17-10s17 4 17 10v6z"/><path d="M17 28l3 6 3-6"/></svg>
    <h3>Beratung &amp; Entwurf</h3>
    <p>Lorem ipsum dolor sit amet, consetetur sadipscing elitr, sed diam nonumy eirmod tempor invidunt ut labore et dolore magna aliquyam erat, sed diam voluptua. At vero eos et accusam et justo duo dolores et ea rebum.</p>
  </div>
  <div class="abs feature" style="left:314px">
    <div class="num" style="left:44px">2.</div>
    <svg width="40" height="44" viewBox="0 0 40 44" fill="none" stroke="#1d5a8a" stroke-width="1.6"><path d="M4 30l18 -8 14 6-18 10z"/><path d="M4 22l18-8 14 6-18 10z" fill="#fff"/><path d="M4 14l18-8 14 6-18 10z" fill="#fff" stroke-dasharray="2 1.5"/></svg>
    <h3>Material &amp; Formenbau</h3>
    <p>Lorem ipsum dolor sit amet, consetetur sadipscing elitr, sed diam nonumy eirmod tempor invidunt ut labore et dolore magna aliquyam erat, sed diam voluptua. At vero eos et accusam et justo duo dolores et ea rebum.</p>
  </div>
  <div class="abs feature" style="left:552px">
    <div class="num" style="left:44px">3.</div>
    <svg width="40" height="44" viewBox="0 0 40 44" fill="none" stroke="#1d5a8a" stroke-width="1.6"><rect x="7" y="6" width="28" height="20"/><path d="M17 11h8"/><rect x="2" y="30" width="36" height="11" rx="5.5"/><circle cx="10" cy="35.5" r="2.5"/><circle cx="20" cy="35.5" r="2.5"/><circle cx="30" cy="35.5" r="2.5"/></svg>
    <h3>Prototyp &amp; Fertigung</h3>
    <div class="kicker">Vorserie - Kleinserie - Serienfertigung</div>
    <p>Lorem ipsum dolor sit amet, consetetur sadipscing elitr, sed diam nonumy eirmod tempor invidunt ut labore et dolore magna aliquyam erat, sed diam voluptua. At vero eos et accusam et justo duo dolores et ea rebum.</p>
  </div>
  <div class="abs btn btn-blue about-btn">Über uns<small>Mehr erfahren <svg width="6" height="8"><path d="M1 1l3 3-3 3" stroke="#fff" stroke-width="1.3" fill="none"/></svg></small></div>

  <!-- trust band -->
  <div class="abs band" role="img" aria-label="Fotocollage: Referenzprojekte mit Pools und Luftfahrtteilen, blau eingefärbt"></div>
  <div class="abs band-title">Unsere Kunden vertrauen<br>auf unsere <strong>Qualität</strong>.</div>
  <div class="abs band-text">Wir sind stolz auf unsere Referenzen und die stetige Zufriedenheit unserer Kunden seit über 20 Jahren. Überzeugen Sie sich von unseren Werken in unserer Referenz-Galerie.</div>
  <div class="abs btn btn-white band-btn">Referenzen<svg width="6" height="8"><path d="M1 1l3 3-3 3" stroke="#1d5a8a" stroke-width="1.3" fill="none"/></svg></div>
  <div class="abs q-mark" style="left:652px;top:664px">“</div>
  <div class="abs q-mark" style="left:465px;top:725px">”</div>
  <blockquote class="abs quote">Lorem ipsum dolor sit amet, consetetur sadipscing elitr, sed diam nonumy eirmod tempor invidunt ut labore et dolore magna aliquyam erat, sed diam voluptua. At vero eos et accusam et justo duo dolores et ea rebum. Stet clita kasd gubergren, no sea takimata sanctus est Lorem ipsum dolor sit amet.</blockquote>
  <div class="abs q-name"><b>Max Mustermann</b><br>Nordwind Aero AG</div>

  <!-- map -->
  <div class="abs map-card"></div>
  <div class="abs map" role="img" aria-label="Karte: Standort Am Werkhof 4"></div>
  <svg class="abs" style="left:385px;top:884px" width="12" height="19" viewBox="0 0 12 19"><path d="M6 18C3 12 1 9 1 6a5 5 0 0110 0c0 3-2 6-5 12z" fill="#e0463b" stroke="#a8261d"/><circle cx="6" cy="6" r="1.8" fill="#8c1c14"/></svg>
  <div class="abs" style="left:397px;top:901px;font-size:6px;font-weight:600;color:#9a1c14">Am Werkhof 4</div>

  <!-- contact -->
  <h2 class="abs h-sec contact-h">Haben Sie Interesse?</h2>
  <div class="abs contact-sub">Zögern Sie bitte nicht uns zu kontaktieren.</div>
  <p class="abs contact-p">Lorem ipsum dolor sit amet, consetetur sadipscing elitr, sed diam nonumy eirmod tempor invidunt ut labore et dolore magna aliquyam erat, sed diam voluptua. At vero eos et accusam et justo duo dolores et ea rebum.</p>
  <div class="abs btn btn-blue contact-btn">Referenzen<svg width="6" height="8"><path d="M1 1l3 3-3 3" stroke="#fff" stroke-width="1.3" fill="none"/></svg></div>
  <div class="abs cinfo" style="left:376px;top:1001px">Telefon<span>+49 (0) 40 / 218 37 60</span></div>
  <div class="abs cinfo" style="left:376px;top:1041px">Fax<span>+49 (0) 40 / 218 37 61</span></div>
  <div class="abs cinfo" style="left:531px;top:1001px">E-Mail<span>info[at]birke-werkstatt.de</span></div>

  <!-- footer -->
  <footer class="abs footer"></footer>
  <div class="abs foot-mark"></div>
  <div class="abs foot-text">Copyright @ 2017 Birke Werkstatt<br><span class="links">Impressum | Allgemeine Geschäftsbedingungen | Kontakt</span></div>

</div>
</body>
</html>
```